Neighbourhood assistance

I need an app design for a social idea. Each person has some skils and could offer some assistance to some of his neighbours. With this app I will bring people together. For free or also for some money.That doesn't matter.

Please have a look into my pptx file which should give you an idea about the upcoming app.

Social

```html
<!DOCTYPE html>
<html lang="en">
<head>
<meta charset="utf-8">
<title>Neighbourhood Assistance – App Screens</title>
<link rel="stylesheet" href="https://fonts.googleapis.com/css2?family=Montserrat:wght@400;500;600&display=swap">
<style>
  :root {
    --canvas: #5c6064;
    --screen-dark: #1b1b1b;
    --navy: #1f3c55;
    --navy-deep: #18304a;
    --photo-warm-a: #8a6a55;
    --photo-warm-b: #3f3a36;
    --photo-green-a: #6f7a45;
    --photo-green-b: #5a4a44;
    --photo-hands-a: #3d3a38;
    --photo-hands-b: #6b5448;
    --avatar-a: #7fae5a;
    --avatar-b: #c9a48a;
    --connect-blue: #3d5b98;
    --white: #ffffff;
    --line: rgba(255,255,255,0.75);
    --placeholder: rgba(255,255,255,0.6);
  }
  * { box-sizing: border-box; margin: 0; padding: 0; }
  html, body { width: 1200px; height: 1000px; overflow: hidden; }
  body {
    background: var(--canvas);
    font-family: "Montserrat", sans-serif;
    color: var(--white);
    position: relative;
  }
  .screen {
    position: absolute;
    width: 194px;
    height: 340px;
    overflow: hidden;
    background: var(--screen-dark);
  }
  .screen--welcome  { left: 66px;  top: 97px; }
  .screen--signin   { left: 345px; top: 97px; }
  .screen--signup   { left: 625px; top: 97px; }
  .screen--home     { left: 66px;  top: 567px; }
  .screen--profile  { left: 345px; top: 567px; }
  .screen--offer    { left: 625px; top: 567px; }

  .screen__photo { position: absolute; inset: 0; }
  .photo--crowd  { background: linear-gradient(170deg, var(--photo-warm-a), var(--photo-warm-b)); }
  .photo--couple { background: linear-gradient(160deg, var(--photo-green-a), var(--photo-green-b)); }
  .photo--hands  { background: linear-gradient(180deg, var(--photo-hands-a), var(--photo-hands-b)); }
  .photo--navy   { background: linear-gradient(180deg, var(--navy), var(--navy-deep)); }

  .el { position: absolute; }
  .app-title {
    left: 0; right: 0; top: 54px;
    text-align: center; font-size: 15.5px; font-weight: 500; line-height: 24px;
  }
  .screen-heading {
    left: 0; right: 0; top: 14px;
    text-align: center; font-size: 8.5px; font-weight: 600;
  }
  .nav-title {
    left: 0; right: 0; top: 21px;
    text-align: center; font-size: 8.5px; letter-spacing: 0.3px;
  }
  .nav-icon { top: 21px; width: 10px; height: 10px; }
  .nav-icon--menu { left: 10px; }
  .nav-icon--search { right: 10px; }

  .field {
    height: 24px; border: 1px solid var(--line); border-radius: 3px;
    font-size: 7.5px; color: var(--placeholder); padding-left: 8px; line-height: 22px;
  }
  .pill {
    height: 18px; border: 1.5px solid var(--white); border-radius: 10px;
    font-size: 8px; text-align: center; line-height: 15px;
  }
  .btn-connect {
    left: 8px; width: 174px; top: 273px; height: 22px;
    background: var(--connect-blue); border-radius: 2px;
    font-size: 6.5px; text-align: center; line-height: 22px; letter-spacing: 0.2px;
  }
  .btn-outline {
    top: 302px; height: 19px; width: 84px;
    border: 1px solid var(--line); border-radius: 2px;
    font-size: 6.5px; text-align: center; line-height: 17px;
  }
  .menu-btn {
    left: 11px; width: 170px; height: 25px;
    border: 1px solid var(--line); border-radius: 2px;
    font-size: 9px; text-align: center; line-height: 23px;
  }
  .note { left: 0; right: 0; text-align: center; font-size: 6.5px; }
  .avatar {
    left: 66px; top: 50px; width: 62px; height: 62px; border-radius: 50%;
    background: radial-gradient(circle at 50% 60%, var(--avatar-b), var(--avatar-a));
  }
  .chip {
    height: 17px; border: 1px solid var(--line); border-radius: 9px;
    font-size: 8px; text-align: center; line-height: 15px;
  }
</style>
</head>
<body>

<!-- Welcome -->
<section class="screen screen--welcome">
  <div class="screen__photo photo--crowd" role="img" aria-label="Photo of a large group of smiling neighbours of all ages"></div>
  <h1 class="el app-title">Neighbourhood<br>Assisstance</h1>
  <div class="el btn-connect">CONNECT WITH CIRCLENET</div>
  <div class="el btn-outline" style="left:8px">SIGN IN</div>
  <div class="el btn-outline" style="left:99px">SIGN UP</div>
</section>

<!-- Sign in -->
<section class="screen screen--signin">
  <div class="screen__photo photo--couple" role="img" aria-label="Photo of two smiling older men outdoors"></div>
  <h2 class="el screen-heading">Neighbourhood Assistance</h2>
  <div class="el field" style="left:12px;width:170px;top:34px">Email address</div>
  <div class="el field" style="left:12px;width:170px;top:66px">Password</div>
  <div class="el pill" style="left:67px;width:60px;top:106px">Let's Go</div>
</section>

<!-- Sign up -->
<section class="screen screen--signup">
  <div class="screen__photo photo--hands" role="img" aria-label="Photo of many hands stacked together"></div>
  <h2 class="el screen-heading">Neighbourhood Assistance</h2>
  <div class="el field" style="left:11px;width:172px;top:34px">Your name</div>
  <div class="el field" style="left:11px;width:172px;top:66px">Email address</div>
  <div class="el field" style="left:11px;width:172px;top:99px">Password</div>
  <div class="el field" style="left:11px;width:172px;top:131px">Confirm password</div>
  <p class="el note" style="top:166px">you can still connect with</p>
  <p class="el note" style="top:178px;font-weight:600">Circlenet</p>
  <div class="el pill" style="left:67px;width:60px;top:199px">Let's Go</div>
</section>

<!-- Home -->
<section class="screen screen--home">
  <div class="screen__photo photo--navy" role="img" aria-label="Navy-tinted photo of a neighbourhood crowd"></div>
  <svg class="el nav-icon nav-icon--menu" viewBox="0 0 10 10"><path d="M0 2h10M0 5h10M0 8h10" stroke="#fff" stroke-width="1"/></svg>
  <h2 class="el nav-title">HOME</h2>
  <svg class="el nav-icon nav-icon--search" viewBox="0 0 10 10"><circle cx="4" cy="4" r="2.8" fill="none" stroke="#fff" stroke-width="1.2"/><path d="M6 6l3 3" stroke="#fff" stroke-width="1.4"/></svg>
  <div class="el menu-btn" style="top:93px">You Offer</div>
  <div class="el menu-btn" style="top:145px">You Need</div>
  <div class="el menu-btn" style="top:197px">Change Profile</div>
</section>

<!-- Change profile -->
<section class="screen screen--profile">
  <div class="screen__photo photo--navy" role="img" aria-label="Navy-tinted photo of a neighbourhood crowd"></div>
  <svg class="el nav-icon nav-icon--menu" viewBox="0 0 10 10"><path d="M0 2h10M0 5h10M0 8h10" stroke="#fff" stroke-width="1"/></svg>
  <h2 class="el nav-title">CHANGE PROFILE</h2>
  <svg class="el nav-icon nav-icon--search" viewBox="0 0 10 10"><circle cx="4" cy="4" r="2.8" fill="none" stroke="#fff" stroke-width="1.2"/><path d="M6 6l3 3" stroke="#fff" stroke-width="1.4"/></svg>
  <div class="el avatar" role="img" aria-label="Profile photo of the user"></div>
  <div class="el field" style="left:14px;width:168px;top:124px">Your full name</div>
  <div class="el field" style="left:14px;width:168px;top:156px">address 1</div>
  <div class="el field" style="left:14px;width:168px;top:188px">address 2</div>
  <div class="el field" style="left:14px;width:168px;top:220px">landmark</div>
  <div class="el pill" style="left:68px;width:60px;top:261px">Save</div>
</section>

<!-- You offer -->
<section class="screen screen--offer">
  <div class="screen__photo photo--navy" role="img" aria-label="Navy-tinted photo of a neighbourhood crowd"></div>
  <svg class="el nav-icon nav-icon--menu" viewBox="0 0 10 10"><path d="M0 2h10M0 5h10M0 8h10" stroke="#fff" stroke-width="1"/></svg>
  <h2 class="el nav-title">YOU OFFER</h2>
  <svg class="el nav-icon nav-icon--search" viewBox="0 0 10 10"><circle cx="4" cy="4" r="2.8" fill="none" stroke="#fff" stroke-width="1.2"/><path d="M6 6l3 3" stroke="#fff" stroke-width="1.4"/></svg>
  <div class="el chip" style="left:26px;width:56px;top:70px">Devices</div>
  <div class="el chip" style="left:89px;width:82px;top:70px">Transportation</div>
  <div class="el chip" style="left:27px;width:69px;top:94px">Tuitions</div>
  <div class="el chip" style="left:101px;width:69px;top:94px">Day Care</div>
  <div class="el chip" style="left:28px;width:78px;top:119px">Babysitting</div>
  <div class="el pill" style="left:67px;width:59px;top:179px">Further</div>
</section>

</body>
</html>
```